NEW YORK Plumbing/utility company 10 year anniversary business card

Looking For simple back and front business card would like to include a few things in description
We offer 24/7 emergency service
residential
commercial
industrial
municipal
services offered
Plumbing
hydro excavation
hydro jetting
Well pumps
Sewer pumps
water mains
sewer mains

```html
<!DOCTYPE html>
<html lang="en">
<head>
<meta charset="utf-8">
<title>Ridgeway Water &amp; Sewer – Business Card</title>
<link href="https://fonts.googleapis.com/css2?family=Oswald:wght@600;700&family=Roboto+Condensed:wght@400;700&display=swap" rel="stylesheet">
<style>
  :root{
    --bg:#d6d6d6;
    --card:#ffffff;
    --brand-blue:#0a5fae;
    --sky-blue:#2fb0e8;
    --alert-red:#e0201b;
    --ink-grey:#7a7a7a;
    --panel-grey:#efefef;
    --rule:#9a9a9a;
  }
  *{box-sizing:border-box;margin:0;padding:0}
  html,body{width:1200px;height:846px;overflow:hidden;background:var(--bg)}
  body{position:relative;font-family:"Roboto Condensed",sans-serif}
  .card{
    position:absolute;top:268px;width:540px;height:310px;background:var(--card);
    box-shadow:0 10px 24px rgba(0,0,0,.18);overflow:hidden;
  }
  .card--front{left:40px}
  .card--back{left:620px}

  /* front */
  .brand{display:flex;align-items:center;gap:12px;position:absolute;left:0;right:0;top:34px;justify-content:center}
  .brand__dot{width:22px;height:22px;border-radius:50%;background:var(--brand-blue)}
  .brand__name{font-family:"Roboto Condensed",sans-serif;font-weight:700;font-size:62px;color:var(--brand-blue);letter-spacing:1px;line-height:1}
  .contact{position:absolute;top:138px;left:0;right:0;display:flex;justify-content:center;gap:26px;color:var(--ink-grey);font-size:25px}
  .contact__item{display:flex;align-items:center;gap:8px}
  .contact__icon{width:26px;height:26px}
  .rule{position:absolute;top:184px;left:70px;right:70px;height:1px;background:var(--rule)}
  .emergency{position:absolute;top:196px;left:0;right:0;text-align:center;font-family:"Oswald",sans-serif;font-weight:700;font-size:24px;color:var(--alert-red);letter-spacing:.3px}
  .sectors{position:absolute;top:246px;left:0;right:0;display:flex;justify-content:center;gap:18px;list-style:none;color:var(--ink-grey);font-size:21px}
  .sectors li{display:flex;align-items:center;gap:7px}
  .drop{width:12px;height:16px;flex:none}

  /* back */
  .panel{position:absolute;right:-60px;top:-40px;width:360px;height:380px;border-radius:50%;background:var(--panel-grey)}
  .services{position:absolute;left:330px;top:34px}
  .services__title{font-family:"Oswald",sans-serif;font-weight:700;font-size:22px;line-height:1;color:var(--sky-blue);margin-bottom:10px}
  .services__list{list-style:none;color:var(--ink-grey);font-size:18px;line-height:1.45}
  .services__list li{display:flex;align-items:center;gap:8px}
  .anniversary{position:absolute;left:44px;top:44px;display:flex;align-items:flex-end;gap:8px}
  .anniversary__num{font-family:"Oswald",sans-serif;font-weight:700;font-size:84px;line-height:.9;color:var(--brand-blue)}
  .anniversary__label{font-family:"Oswald",sans-serif;font-weight:600;font-size:20px;line-height:1;color:var(--ink-grey);padding-bottom:6px}
  .anniversary__label small{display:block;font-size:10px;letter-spacing:1.5px;margin-top:3px}
  .lockup{position:absolute;left:44px;top:168px}
  .lockup__name{display:flex;align-items:center;gap:10px;font-weight:700;font-size:44px;line-height:1;color:var(--brand-blue)}
  .lockup__sub{font-weight:700;font-size:22px;letter-spacing:3px;color:var(--brand-blue);margin-top:10px}
</style>
</head>
<body>
  <svg width="0" height="0" style="position:absolute">
    <defs>
      <symbol id="drop" viewBox="0 0 12 16"><path d="M6 0 C6 0 0 7 0 10.5 A6 6 0 0 0 12 10.5 C12 7 6 0 6 0Z"/></symbol>
    </defs>
  </svg>

  <section class="card card--front">
    <div class="brand">
      <span class="brand__dot"></span>
      <span class="brand__name">Ridgeway</span>
    </div>
    <div class="contact">
      <span class="contact__item">
        <svg class="contact__icon" viewBox="0 0 26 26"><circle cx="13" cy="13" r="13" fill="var(--brand-blue)"/><path d="M9 7c1 0 2 2 2 3s-1 1-1 2 2 3 3 3 1-1 2-1 3 1 3 2-1 3-3 3c-4 0-8-4-8-8 0-2 1-4 2-4z" fill="#fff"/></svg>
        845 555 0182
      </span>
      <span class="contact__item">
        <svg class="contact__icon" viewBox="0 0 26 26"><circle cx="13" cy="13" r="13" fill="var(--brand-blue)"/><rect x="6" y="8" width="14" height="10" fill="none" stroke="#fff" stroke-width="1.6"/><path d="M6 8l7 6 7-6" fill="none" stroke="#fff" stroke-width="1.6"/></svg>
        info@ridgewayny.com
      </span>
    </div>
    <div class="rule"></div>
    <p class="emergency">WE OFFER 24/7 EMERGENCY SERVICE</p>
    <ul class="sectors">
      <li><svg class="drop" fill="var(--alert-red)"><use href="#drop"/></svg>residential</li>
      <li><svg class="drop" fill="var(--alert-red)"><use href="#drop"/></svg>commercial</li>
      <li><svg class="drop" fill="var(--alert-red)"><use href="#drop"/></svg>industrial</li>
      <li><svg class="drop" fill="var(--alert-red)"><use href="#drop"/></svg>municipal</li>
    </ul>
  </section>

  <section class="card card--back">
    <div class="panel"></div>
    <div class="anniversary">
      <span class="anniversary__num">10</span>
      <span class="anniversary__label">YEARS<small>ANNIVERSARY</small></span>
    </div>
    <div class="lockup">
      <div class="lockup__name">Ridgeway</div>
      <div class="lockup__sub">WATER &amp; SEWER</div>
    </div>
    <div class="services">
      <h2 class="services__title">SERVICES<br>OFFERED</h2>
      <ul class="services__list">
        <li><svg class="drop" fill="var(--sky-blue)"><use href="#drop"/></svg>Plumbing</li>
        <li><svg class="drop" fill="var(--sky-blue)"><use href="#drop"/></svg>Hydro excavation</li>
        <li><svg class="drop" fill="var(--sky-blue)"><use href="#drop"/></svg>Hydro jetting</li>
        <li><svg class="drop" fill="var(--sky-blue)"><use href="#drop"/></svg>Well pumps</li>
        <li><svg class="drop" fill="var(--sky-blue)"><use href="#drop"/></svg>Sewer pumps</li>
        <li><svg class="drop" fill="var(--sky-blue)"><use href="#drop"/></svg>Sewer mains</li>
        <li><svg class="drop" fill="var(--sky-blue)"><use href="#drop"/></svg>Water mains</li>
      </ul>
    </div>
  </section>
</body>
</html>
```